Business Card design for construction company

I would like a business card design for a construction company - Harlow Constructions. I have attached the ai logo file for use. I would like the card to be very smart and clean and incorporate only white and the two colours in the logo. I would like the card to have two sides. One side can just have the logo, the other with the relevant information.

Target Market(s)

Building and Construction Clients

Industry/Entity Type

Business

Contact Information for Business Card

Name: Tom Pardoe
Company: Harlow Constructions Pty Limited
Address: 14 Mallee Crescent Carrow Vale 2093
Phone: 0427 531 068
Email: tomp@harlowbuild-example.com.au

Font styles to use
Serif
Sans Serif

Requirements
Must have
• Details noted above
• Logo as provided
• Colours as in logo
• Square edges
• A font that compliments the logo
Should not have
• Any colour other than white and those in logo
• Rounded edges

```html
<!DOCTYPE html>
<html lang="en">
<head>
<meta charset="utf-8">
<title>Harlow Constructions – Business Card</title>
<link rel="stylesheet" href="https://fonts.googleapis.com/css2?family=Michroma&family=Arimo:wght@400;700&display=swap">
<style>
  :root {
    --backdrop: #3a3a3a;
    --card-white: #ffffff;
    --card-grey: #595a5c;
    --ink-dark: #5a5b5d;
    --ink-light: #ffffff;
    --accent-blue: #1ea0e0;
    --rule: #a9abad;
  }
  * { box-sizing: border-box; margin: 0; padding: 0; }
  html, body {
    width: 1200px;
    height: 900px;
    overflow: hidden;
    background: var(--backdrop);
  }
  .canvas {
    width: 1200px;
    height: 900px;
    display: flex;
    flex-direction: column;
    align-items: center;
    justify-content: center;
    gap: 48px;
  }
  .card {
    position: relative;
    width: 560px;
    height: 320px;
    overflow: hidden;
    box-shadow: 0 10px 30px rgba(0,0,0,0.35);
  }
  .card--front { background: var(--card-white); }
  .card--back { background: var(--card-grey); }

  .wordmark {
    position: absolute;
    display: flex;
    align-items: center;
    gap: 12px;
    font-family: "Michroma", sans-serif;
    font-weight: 400;
    letter-spacing: 0.1em;
    text-transform: uppercase;
    white-space: nowrap;
  }
  .wordmark__square {
    width: 10px;
    height: 10px;
    background: var(--accent-blue);
    flex: none;
  }
  .card--front .wordmark {
    left: 50%;
    top: 50%;
    transform: translate(-50%, -50%);
    font-size: 18px;
    color: var(--ink-dark);
  }
  .card--back .wordmark {
    left: 48px;
    top: 60px;
    font-size: 18px;
    color: var(--ink-light);
  }
  .divider {
    position: absolute;
    left: 48px;
    right: 48px;
    top: 112px;
    height: 1px;
    background: var(--rule);
  }
  .contact {
    position: absolute;
    left: 48px;
    right: 48px;
    top: 136px;
    font-family: "Arimo", sans-serif;
    color: var(--ink-light);
  }
  .contact__name {
    font-weight: 700;
    font-size: 16px;
    letter-spacing: 0.14em;
    text-transform: uppercase;
    margin-bottom: 12px;
  }
  .contact__line {
    font-size: 14px;
    line-height: 1.6;
    letter-spacing: 0.02em;
  }
</style>
</head>
<body>
  <main class="canvas">
    <section class="card card--front" aria-label="Card front">
      <div class="wordmark">
        <span class="wordmark__square" aria-hidden="true"></span>
        <span class="wordmark__name">Harlow Constructions</span>
      </div>
    </section>

    <section class="card card--back" aria-label="Card back">
      <div class="wordmark">
        <span class="wordmark__square" aria-hidden="true"></span>
        <span class="wordmark__name">Harlow Constructions</span>
      </div>
      <div class="divider"></div>
      <div class="contact">
        <p class="contact__name">Tom Pardoe</p>
        <p class="contact__line">14 Mallee Crescent Carrow Vale 2093</p>
        <p class="contact__line">0427 531 068</p>
        <p class="contact__line">tomp@harlowbuild-example.com.au</p>
      </div>
    </section>
  </main>
</body>
</html>
```